Stationery Design for Information Technology Company
Stationery Design
Stationery Design for Information Technology Company - Information Technology
Creative Brief
Professional
Kamal Dutta
President / CEO
58 Pell Road East, Suite 240 Cedarvale, OH 08917
kamal@greyoaksys.com
www.greyoaksys.com
Please use the Ai file uploaded BUT WITHOUT THE TAGLINE
On the card only mention "GREY OAK LOGO" NO NEED FOR "SOFTWARE SERVICES" I want the logo displayed on the front and back of the card with a back ground color that goes along with the logo design. I want the logo to be centrally located at the back of the card. THE LOGO SHOULD BE ON FRONT AND BACK. ON THE BACK IT SHOULD BE A FULL LOGO, WITH MY THREE OFFICES 1) USA 2)INDIA 3) AUSTRALIA

```html
<!DOCTYPE html>
<html lang="en">
<head>
<meta charset="utf-8">
<title>Grey Oak Business Card</title>
<link rel="stylesheet" href="https://fonts.googleapis.com/css2?family=Open+Sans:wght@400;600;700;800&display=swap">
<style>
  :root {
    --bg: #e9ebee;
    --navy: #16305c;
    --blue: #1f4f8f;
    --blue-deep: #193f75;
    --accent: #2f7fc6;
    --ink: #2b3440;
    --muted: #4a5360;
    --paper: #ffffff;
    --logo-light: #c7d4e5;
  }
  * { margin: 0; padding: 0; box-sizing: border-box; }
  html, body {
    width: 1200px; height: 901px; overflow: hidden;
    background: var(--bg);
    font-family: "Open Sans", Arial, sans-serif;
  }
  .stage { position: relative; width: 1200px; height: 901px; }

  .card {
    position: absolute;
    border-radius: 18px;
    overflow: hidden;
    box-shadow: 0 10px 28px rgba(20, 30, 50, 0.22);
  }

  /* Back side */
  .card-back {
    left: 70px; top: 100px; width: 540px; height: 310px;
    background: linear-gradient(160deg, var(--blue) 0%, var(--blue-deep) 100%);
    color: #fff;
    text-align: center;
  }
  .card-back .wordmark {
    position: absolute; left: 0; right: 0; top: 104px;
    font-weight: 800; font-size: 52px; letter-spacing: -1px;
    color: var(--logo-light);
  }
  .offices {
    position: absolute; left: 0; right: 0; top: 200px;
    font-size: 12px; letter-spacing: 0.5px;
  }
  .offices .label { text-decoration: underline; margin-bottom: 6px; }
  .offices .list span { padding: 0 10px; }
  .offices .list span + span { border-left: 1px solid rgba(255,255,255,0.8); }

  /* Front side */
  .card-front {
    left: 540px; top: 460px; width: 600px; height: 345px;
    background: var(--paper);
  }
  .brand {
    position: absolute; left: 38px; top: 120px;
    display: flex; align-items: center; gap: 8px;
  }
  .brand .mark { width: 14px; height: 14px; background: var(--accent); }
  .brand .wordmark {
    font-weight: 800; font-size: 46px; letter-spacing: -1px; color: var(--ink);
  }
  .contact {
    position: absolute; left: 345px; top: 58px;
    color: var(--muted); font-size: 13px; line-height: 1.35;
  }
  .contact .name { color: var(--blue); font-weight: 700; font-size: 15px; }
  .contact .title { margin-bottom: 18px; }
  .contact .address { margin-bottom: 18px; }
  .contact .line { display: flex; align-items: center; gap: 8px; }
  .contact .line svg { width: 13px; height: 13px; fill: var(--ink); }
  .contact .email { margin-top: 2px; }

  .footer-band { position: absolute; left: 0; bottom: 0; width: 600px; height: 60px; }
  .web {
    position: absolute; right: 40px; bottom: 14px;
    color: #fff; font-size: 14px; letter-spacing: 3px;
  }
</style>
</head>
<body>
<main class="stage">

  <section class="card card-back" aria-label="Card back">
    <div class="wordmark">GREY OAK</div>
    <div class="offices">
      <p class="label">Our Offices in:</p>
      <p class="list"><span>USA</span><span>INDIA</span><span>AUSTRALIA</span></p>
    </div>
  </section>

  <section class="card card-front" aria-label="Card front">
    <div class="brand">
      <span class="mark"></span>
      <span class="wordmark">GREY OAK</span>
    </div>

    <div class="contact">
      <p class="name">Kamal Dutta</p>
      <p class="title">President / CEO</p>
      <p class="address">58 Pell Road East, Suite 240<br>Cedarvale, OH 08917</p>
      <p class="line">
        <svg viewBox="0 0 16 16"><path d="M3 1h3l1.5 4-2 1.3a9 9 0 0 0 4.2 4.2L11 8.5 15 10v3a2 2 0 0 1-2 2A12 12 0 0 1 1 3a2 2 0 0 1 2-2z"/></svg>
        614-555-0148
      </p>
      <p class="line">
        <svg viewBox="0 0 16 16"><path d="M4 0h8a1 1 0 0 1 1 1v14a1 1 0 0 1-1 1H4a1 1 0 0 1-1-1V1a1 1 0 0 1 1-1zm1 2v10h6V2zm3 11a1 1 0 1 0 0 2 1 1 0 0 0 0-2z"/></svg>
        614-555-0193
      </p>
      <p class="line">
        <svg viewBox="0 0 16 16"><path d="M4 0h7l2 2v4h1a2 2 0 0 1 2 2v6H0V8a2 2 0 0 1 2-2h2zm1 1v5h7V2.5L10.5 1zM3 10v1h10v-1z"/></svg>
        614-555-0126
      </p>
      <p class="email">kamal@greyoaksys.com</p>
    </div>

    <svg class="footer-band" viewBox="0 0 600 60" preserveAspectRatio="none" aria-hidden="true">
      <path d="M0 44 H280 C300 44 305 22 330 22 H600 V60 H0 Z" fill="var(--accent)"/>
      <path d="M0 50 H285 C305 50 312 28 338 28 H600 V60 H0 Z" fill="var(--navy)"/>
    </svg>
    <p class="web">www.greyoaksys.com</p>
  </section>

</main>
</body>
</html>
```